Job advert for Forged Here Collective

I would like a poster graphic that I can promote on social media to advertise a job vacancy we will be promoting our upcoming jobs, here is the text...

WE ARE ON THE…

LOOKOUT
(maybe insert graphic or icon that fits with the message here)

For A

OPERATIONS AND HR MANAGER

MEMBERSHIP ADVISOR (EAST MIDLANDS)

SOCIAL MEDIA CONTENT CREATOR

THE UK’s FASTEST GROWING NETWORK FOR MANUFACTURERS

OFFICES IN BIRMINGHAM AND LEEDS - WE ARE AN INCLUSIVE EMPLOYER (use the equality logo provided here)

Target Market(s)

people looking to find a new job

Industry/Entity Type

Manufacture

Font styles to use
Sans Serif

Colors
f04a50
f68e4e
e667a6

Requirements
Must have
• Clear simple and contemporary style
Nice to have
• a nice graphic or icon to convey the text message
Should not have
• use of dark depressing colours

```html
<!DOCTYPE html>
<html lang="en">
<head>
<meta charset="utf-8">
<title>Forged Here Collective – We Are On The Lookout</title>
<link rel="stylesheet" href="https://fonts.googleapis.com/css2?family=Anton&family=Arimo:wght@400;700&display=swap">
<style>
  :root {
    --orange: #f6844c;
    --orange-light: #f89a66;
    --orange-soft: #f9ab7c;
    --ink: #111111;
    --white: #ffffff;
    --rule: rgba(255, 255, 255, 0.35);
    --lime: #a3cf3a;
    --red: #e3262e;
    --badge: #f04a50;
  }
  * { margin: 0; padding: 0; box-sizing: border-box; }
  html, body { width: 927px; height: 1200px; overflow: hidden; }
  body { background: var(--white); font-family: "Arimo", Arial, sans-serif; }

  .poster {
    position: relative;
    width: 927px;
    height: 1200px;
    background: var(--orange);
    overflow: hidden;
  }

  .hero-illustration {
    position: absolute;
    left: 45px;
    top: 20px;
    width: 845px;
    height: 440px;
    border-radius: 24px;
    background: radial-gradient(ellipse at 62% 40%, var(--orange-soft) 0%, var(--orange-light) 45%, var(--orange) 80%);
  }

  .kicker {
    position: absolute;
    left: 67px;
    top: 468px;
    font-weight: 700;
    font-size: 39px;
    line-height: 1;
    color: var(--ink);
    white-space: nowrap;
  }

  .headline {
    position: absolute;
    left: 66px;
    top: 528px;
    font-family: "Anton", Impact, sans-serif;
    font-weight: 400;
    font-size: 158px;
    line-height: 1;
    color: var(--white);
    letter-spacing: 1px;
    white-space: nowrap;
    transform: scaleX(1.43);
    transform-origin: left top;
    text-shadow: 2px 4px 0 rgba(120, 50, 20, 0.25);
  }

  .lead-in {
    position: absolute;
    left: 67px;
    top: 716px;
    font-weight: 700;
    font-size: 22px;
    line-height: 1;
    color: var(--ink);
  }

  .vacancies {
    position: absolute;
    left: 67px;
    top: 752px;
    width: 554px;
    list-style: none;
  }
  .vacancies li {
    height: 56px;
    display: flex;
    align-items: center;
    font-weight: 700;
    font-size: 24px;
    color: var(--white);
    white-space: nowrap;
    border-bottom: 1px dotted var(--rule);
  }
  .vacancies li:last-child { border-bottom: none; }

  .tagline {
    position: absolute;
    left: 67px;
    top: 953px;
    font-weight: 700;
    font-size: 21px;
    line-height: 29px;
    color: var(--ink);
    white-space: nowrap;
  }

  .footer-band {
    position: absolute;
    left: 0;
    top: 1027px;
    width: 927px;
    height: 149px;
    background: var(--white);
  }

  .inclusion-badge {
    position: absolute;
    left: 67px;
    top: 30px;
    width: 90px;
    height: 90px;
    border-radius: 50%;
    background: var(--badge);
  }

  .brand {
    position: absolute;
    top: 44px;
    display: flex;
    align-items: center;
    gap: 12px;
    font-weight: 700;
    font-size: 24px;
    line-height: 28px;
    white-space: nowrap;
  }
  .brand-mark { width: 60px; height: 60px; border-radius: 50%; flex: none; }
  .brand--north { left: 345px; color: var(--lime); }
  .brand--north .brand-mark { background: var(--lime); }
  .brand--central { left: 630px; color: var(--red); }
  .brand--central .brand-mark { background: var(--red); }
</style>
</head>
<body>
  <main class="poster">
    <div class="hero-illustration" role="img" aria-label="Illustration of a cheerful office worker looking through a telescope among colourful clouds"></div>

    <p class="kicker">WE ARE ON THE…</p>
    <h1 class="headline">LOOKOUT</h1>

    <p class="lead-in">For A</p>
    <ul class="vacancies">
      <li>OPERATIONS AND HR MANAGER</li>
      <li>MEMBERSHIP ADVISOR (EAST MIDLANDS)</li>
      <li>SOCIAL MEDIA CONTENT CREATOR</li>
    </ul>

    <p class="tagline">The UK’s Fastest Growing Network For Manufacturers<br>Offices In Birmingham And Leeds - We Are An Inclusive Employer</p>

    <footer class="footer-band">
      <div class="inclusion-badge" role="img" aria-label="Inclusive employer badge"></div>
      <div class="brand brand--north"><span class="brand-mark"></span><span>FORGED HERE<br>NORTH</span></div>
      <div class="brand brand--central"><span class="brand-mark"></span><span>FORGED HERE<br>CENTRAL</span></div>
    </footer>
  </main>
</body>
</html>
```